Medical equipment business looking for professional, unique business card

We need a business card design for a durable medical equipment company. We are small but would like our cards to express that we are much bigger. We focus on braces (back, knee, wrist, etc) but also do crutches, rollators, wheelchairs- basically medical equipment that gets you going and back in Action. Our colors are blue and green and our logo has an arrow and use of a "spine". We'd like to express professionalism while being unique.

Industry/Entity Type

Medical Equipment

Contact Information for Business Card

Professional feel but unique. Memorable.

Font styles to use
Serif
Sans Serif
Other font styles liked:
• verdana

Requirements
Must have
• card holders cell#, business phone#, fax#, email, website address, business address, logo
Nice to have
• use of medical/healthcare related descriptive words, items, look
Should not have
• the wrong colors or cartoon characters.

```html
<!DOCTYPE html>
<html lang="en">
<head>
<meta charset="utf-8">
<title>Kinetra DME – Business Card</title>
<link rel="stylesheet" href="https://fonts.googleapis.com/css2?family=Source+Sans+3:wght@400;600;700&display=swap">
<style>
  :root {
    --navy: #06466b;
    --green: #8cc63f;
    --white: #ffffff;
    --ink: #222a30;
    --stage: #3b3b3b;
  }
  html, body {
    margin: 0;
    padding: 0;
    width: 1200px;
    height: 1200px;
    overflow: hidden;
    background: var(--stage);
    font-family: "Source Sans 3", Verdana, sans-serif;
  }
  .canvas {
    position: relative;
    width: 1200px;
    height: 1200px;
  }
  .card {
    position: absolute;
    left: 250px;
    width: 702px;
    height: 398px;
    box-sizing: border-box;
  }
  .card-front {
    top: 178px;
    background: var(--navy);
    border-radius: 0 80px 0 80px;
  }
  .card-back {
    top: 624px;
    background: var(--white);
    border-radius: 80px 0 80px 0;
  }
  .brand {
    position: absolute;
    display: flex;
    align-items: center;
    gap: 14px;
    font-weight: 600;
    white-space: nowrap;
  }
  .brand-dot {
    width: 22px;
    height: 22px;
    border-radius: 50%;
    background: var(--green);
    flex: none;
  }
  .card-front .brand {
    left: 50%;
    top: 50%;
    transform: translate(-50%, -50%);
    font-size: 60px;
    color: var(--white);
  }
  .card-back .brand {
    right: 32px;
    top: 62px;
    font-size: 48px;
    color: var(--navy);
  }
  .holder {
    position: absolute;
    right: calc(702px - 188px);
    top: 236px;
    text-align: right;
  }
  .holder-name {
    font-size: 26px;
    font-weight: 700;
    color: var(--navy);
    line-height: 1.1;
  }
  .holder-title {
    font-size: 18px;
    color: var(--ink);
    margin-top: 2px;
  }
  .divider {
    position: absolute;
    left: 224px;
    top: 182px;
    width: 1.5px;
    height: 168px;
    background: var(--green);
  }
  .contacts {
    position: absolute;
    left: 262px;
    top: 198px;
    margin: 0;
    padding: 0;
    list-style: none;
    font-size: 18px;
    color: var(--ink);
  }
  .contacts li {
    display: flex;
    align-items: center;
    height: 23.5px;
  }
  .contacts svg {
    width: 16px;
    height: 16px;
    margin-right: 12px;
    flex: none;
  }
  .address {
    position: absolute;
    left: 265px;
    top: 324px;
    font-size: 18px;
    color: var(--ink);
  }
</style>
</head>
<body>
<main class="canvas">
  <section class="card card-front">
    <div class="brand"><span class="brand-dot"></span>Kinetra DME</div>
  </section>

  <section class="card card-back">
    <div class="brand"><span class="brand-dot"></span>Kinetra DME</div>

    <div class="holder">
      <div class="holder-name">Daniel Reyes</div>
      <div class="holder-title">Doctor</div>
    </div>

    <div class="divider"></div>

    <ul class="contacts">
      <li>
        <svg viewBox="0 0 16 16" aria-hidden="true"><rect x="4" y="1" width="8" height="14" rx="1.5" fill="none" stroke="#8cc63f" stroke-width="1.6"/><circle cx="8" cy="12.5" r="0.9" fill="#8cc63f"/></svg>
        (000) 000-0000
      </li>
      <li>
        <svg viewBox="0 0 16 16" aria-hidden="true"><path d="M1 6c0-2 3-3 7-3s7 1 7 3v1h-3V5.5H4V7H1z" fill="#8cc63f"/><path d="M3 9l2-2h6l2 2v5H3z" fill="#8cc63f"/><circle cx="8" cy="11" r="1.6" fill="#fff"/></svg>
        (555) 210-4417
      </li>
      <li>
        <svg viewBox="0 0 16 16" aria-hidden="true"><rect x="4" y="1" width="8" height="4" fill="#8cc63f"/><rect x="1" y="5.5" width="14" height="6" rx="1.5" fill="#8cc63f"/><rect x="4" y="10" width="8" height="5" fill="#8cc63f" stroke="#fff" stroke-width="1"/></svg>
        (555) 210-4480
      </li>
      <li>
        <svg viewBox="0 0 16 16" aria-hidden="true"><rect x="1" y="3" width="14" height="10" fill="#8cc63f"/><path d="M1 3l7 6 7-6M1 13l5-5M15 13l-5-5" fill="none" stroke="#fff" stroke-width="1.2"/></svg>
        dreyes@kinetradme.com
      </li>
      <li>
        <svg viewBox="0 0 16 16" aria-hidden="true"><g fill="none" stroke="#8cc63f" stroke-width="1.2"><circle cx="8" cy="8" r="6.5"/><ellipse cx="8" cy="8" rx="3" ry="6.5"/><path d="M1.5 8h13M2.5 4.8h11M2.5 11.2h11"/></g></svg>
        www.kinetradme.com
      </li>
    </ul>

    <div class="address">48 Linden Ave #2, Fairview, TN 37062</div>
  </section>
</main>
</body>
</html>
```